International Fleet Management Firm Website

HaulvergeKenda is a Fleet Management Company that provides insight into customers fleets. We do this through web tools which we have developed which function through a client login screen to help ensure that corporates are able to stay on top of their fleets 24/7.
We are about to launch and are looking for a great new website to help us come out with bang! We would like a site that matches our values of ; Courage, integrity and leadership.
Although we have developed the app. We would also like to redesign the look of the site on the back end.
(1) We need to incorporate the new corporate colours
(2) Would like to create a better user experience.
The site that I would like to model ours after is;
www.brellix.com (usa version)
Good Luck!!
Updates
Jusst added the .png version of the logo. Hopes this helps!
Industry/Entity Type
It Company
Look and feel

```html
<!DOCTYPE html>
<html lang="en">
<head>
<meta charset="utf-8">
<title>HaulvergeKenda – Fleet Management</title>
<link href="https://fonts.googleapis.com/css2?family=Arimo:wght@400;700&display=swap" rel="stylesheet">
<style>
:root{
  --bg-deep:#062a58;
  --bg-mid:#0b4f94;
  --accent:#1fa0d8;
  --accent-light:#3fc0f0;
  --nav-top:#2a93c4;
  --nav-bottom:#13638f;
  --panel-dark:#1b1d1f;
  --panel-darker:#131415;
  --ink:#1a1a1a;
  --muted:#444;
  --white:#ffffff;
  --grey-logo:#8a8a8a;
}
*{margin:0;padding:0;box-sizing:border-box}
html,body{width:1124px;height:1200px;overflow:hidden}
body{
  position:relative;font-family:"Arimo",Arial,sans-serif;color:var(--ink);
  background:radial-gradient(ellipse at 50% 35%,var(--bg-mid) 0%,var(--bg-deep) 70%,#041d40 100%);
}
.abs{position:absolute}
.social{top:0;width:30px;height:28px;background:#2c6fb0;border:2px solid #5aa0e0;border-top:none}
.logo-tab{left:174px;top:34px;width:284px;height:84px;background:var(--white);clip-path:polygon(0 0,74% 0,100% 100%,0 100%);border-radius:8px 0 0 0}
.brand{left:212px;top:74px;font-size:21px;font-weight:700;color:#1b6fa8;letter-spacing:-.5px}
.brand-mark{left:277px;top:40px;width:28px;height:28px;border-radius:50%;background:#1b6fa8}
.tagline{left:233px;top:104px;font-size:6px;color:#777;letter-spacing:1px}
.top-bar{left:380px;top:52px;width:568px;height:66px;background:var(--panel-dark);border-radius:0 8px 0 0;clip-path:polygon(0 0,100% 0,100% 100%,13.5% 100%)}
.login-label{left:727px;top:56px;font-size:11px;color:var(--accent-light)}
.login-label span{color:var(--white)}
.field{top:74px;height:20px;background:linear-gradient(#8b8b8b,#666);color:#fff;font-size:10px;padding:5px 6px}
.signin{left:890px;top:74px;width:46px;height:20px;background:linear-gradient(#2aa8e0,#1273b0);color:#fff;font-size:10px;text-align:center;padding-top:5px;border:1px solid #7fd0f5}
.forgot{left:727px;top:99px;font-size:11px;color:#ddd}
.forgot span{color:var(--accent-light)}
.nav{left:174px;top:118px;width:776px;height:44px;background:linear-gradient(var(--nav-top),var(--nav-bottom));display:flex;align-items:center;padding-left:12px;gap:30px}
.nav a{color:#fff;font-size:16px;text-decoration:none}
.search{left:802px;top:124px;width:131px;height:30px;background:linear-gradient(#fff,#d9d9d9);border-radius:3px;font-size:11px;padding:10px 0 0 13px}
.search svg{position:absolute;right:8px;top:5px}
.hero-photo{left:174px;top:162px;width:520px;height:343px;background:linear-gradient(110deg,#c9d2dc 0%,#eef1f4 40%,#a9b4c0 70%,#5d6874 100%)}
.hero-panel{left:694px;top:162px;width:256px;height:343px;background:linear-gradient(135deg,#fbfcfd,#e2e7ec)}
.hero-title{left:724px;top:227px;font-size:24px;font-weight:700}
.hero-sub{left:724px;top:254px;font-size:24px;color:var(--accent)}
.hero-copy{left:728px;top:292px;width:188px;font-size:9px;line-height:11.5px;text-align:justify}
.read-more{height:24px;background:var(--panel-dark);color:#fff;font-size:11px;padding:6px 0 0 6px;clip-path:polygon(0 0,100% 0,76% 100%,0 100%);border-radius:3px 0 0 3px}
.pager{left:630px;top:478px;width:128px;height:27px;background:linear-gradient(#fff,#d2d6da);clip-path:polygon(6% 0,94% 0,100% 100%,0 100%);display:flex;align-items:center;justify-content:center;gap:4px}
.pager i{width:10px;height:10px;border-radius:50%;background:#8a9098;display:block}
.pager i.on{background:#2c3238}
.pager b{color:#777;font-weight:400;font-size:16px;margin:0 6px}
.features{left:172px;top:520px;width:780px;height:300px;background:linear-gradient(#fff 45%,#aeb1b4);border:1px solid #d0d4d8}
.card-img{top:537px;width:177px;height:128px;border:1px solid #ddd}
.card-h{font-size:18px;font-weight:700;line-height:24px}
.card-h span{display:block;font-weight:400;color:var(--accent)}
.card-copy{width:174px;font-size:9px;line-height:11.3px;text-align:justify;color:#222}
.footer-zone{left:176px;top:820px;width:772px;height:348px;background:var(--panel-dark);border-radius:0 0 8px 8px}
.help{left:191px;top:839px;width:175px;height:186px;background:linear-gradient(#1d8ec6,#0f5f8c);border-radius:4px}
.help-h{left:198px;top:842px;font-size:22px;line-height:25px;color:#7fd6ff;font-weight:700}
.help-h span{color:#fff;font-weight:400}
.help-h em{font-style:normal;font-weight:400;color:#333}
.help-line{left:198px;top:894px;width:158px;border-top:1px dotted #9dd8f5}
.help-sub{left:198px;top:900px;font-size:11px;color:#d8f0ff}
.help-hours{left:198px;top:936px;font-size:9px;line-height:11.5px;color:#fff}
.chat{left:198px;top:992px;width:94px;height:24px;background:var(--panel-darker);color:var(--accent-light);font-size:11px;padding:6px 0 0 5px;clip-path:polygon(0 0,100% 0,78% 100%,0 100%)}
.address{left:192px;top:1038px;font-size:11px;line-height:14.5px;color:#fff}
.address span{color:var(--accent-light)}
.foot-social{top:1102px;width:20px;height:20px;background:#777}
.clients{left:380px;top:841px;width:553px;height:252px;background:var(--panel-darker);border-radius:4px}
.sec-h{font-size:19px;color:#fff;font-weight:700}
.sec-h span{color:var(--accent-light);font-weight:400}
.dots{width:520px;border-top:1px dotted #555}
.client-name{top:919px;font-size:18px;font-weight:700;color:var(--grey-logo)}
.review{left:396px;top:1012px;font-size:11px;line-height:13px;color:#e8e8e8;white-space:nowrap}
.review-dots{color:var(--accent)}
.reviewer{left:771px;top:1044px;font-size:11px;line-height:14px;color:#ddd}
.reviewer span{color:var(--accent-light)}
.find-more{left:396px;top:1063px;width:94px;height:25px;background:linear-gradient(#1d8ec6,#0f5f8c);color:#fff;font-size:11px;padding:7px 0 0 5px;clip-path:polygon(0 0,100% 0,78% 100%,0 100%)}
.foot-nav{left:191px;top:1139px;display:flex;gap:19px;font-size:11px;color:#fff}
.copyright{left:732px;top:1139px;font-size:11px;color:#fff}
</style>
</head>
<body>
<div class="abs social" style="left:882px"></div>
<div class="abs social" style="left:920px"></div>

<header>
  <div class="abs top-bar"></div>
  <div class="abs logo-tab"></div>
  <div class="abs brand-mark"></div>
  <div class="abs brand">HaulvergeKenda</div>
  <div class="abs tagline">Every Route In Plain View</div>
  <div class="abs login-label">Client Login<span>:</span></div>
  <div class="abs field" style="left:727px;width:72px">User ID</div>
  <div class="abs field" style="left:812px;width:72px">Password</div>
  <div class="abs signin">Sign in</div>
  <div class="abs forgot">Forget Password? <span>Register now</span></div>
  <nav class="abs nav">
    <a>Who we are</a><a>Services</a><a>Careers</a><a>Owners</a><a>Our Updates</a><a>Contact Us</a>
  </nav>
  <div class="abs search">Search.....
    <svg width="24" height="22" viewBox="0 0 24 22"><circle cx="9" cy="9" r="6" fill="none" stroke="#1a9ad6" stroke-width="3"/><line x1="13" y1="13" x2="21" y2="20" stroke="#1a9ad6" stroke-width="4" stroke-linecap="round"/></svg>
  </div>
</header>

<section class="hero">
  <div class="abs hero-photo" role="img" aria-label="White delivery van driving along a harbour road with cranes in the background"></div>
  <div class="abs hero-panel"></div>
  <div class="abs hero-title">LOREM IPSUM</div>
  <div class="abs hero-sub">Dolor sit amet</div>
  <p class="abs hero-copy">Lorem ipsum dolor sit amet, consectetuer adipiscing elit, sed diam nonummy nibh euismod tincidunt ut laoreet dolore magna aliquam erat volutpat. Ut wisi enim ad minim veniam, quis nostrud exerci tation ullamcorper suscipit lobortis nisl ut aliquip ex ea commodo consequat.</p>
  <div class="abs read-more" style="left:722px;top:421px;width:96px">READ MORE</div>
  <div class="abs pager"><b>‹</b><i></i><i></i><i class="on"></i><i></i><b>›</b></div>
</section>

<section class="abs features"></section>
<div class="abs card-img" style="left:189px;background:linear-gradient(135deg,#6a3c44,#3ab6e0 45%,#1c8cc0)" role="img" aria-label="Row of blue fleet cars"></div>
<div class="abs card-img" style="left:380px;background:linear-gradient(135deg,#5a4a3a,#d8d4ce 45%,#7a7068)" role="img" aria-label="Glass award trophy"></div>
<div class="abs card-img" style="left:569px;background:linear-gradient(135deg,#7a5a30,#c8902e 45%,#e8c020)" role="img" aria-label="Safety boots and yellow hard hat"></div>
<div class="abs card-img" style="left:762px;background:linear-gradient(#8aa0b8,#4a5870 55%,#9a9a9a)" role="img" aria-label="Crew pulling cargo across a deck"></div>

<div class="abs card-h" style="left:191px;top:673px">Welcome to<span>Our World</span></div>
<div class="abs card-h" style="left:382px;top:670px">Awards<span>Achievements</span></div>
<div class="abs card-h" style="left:570px;top:673px">Safe way to<span>Contentment</span></div>
<div class="abs card-h" style="left:763px;top:673px">Our Latest<span>News</span></div>

<p class="abs card-copy" style="left:191px;top:724px">Lorem ipsum dolor sit amet, consectetuer adipiscing elit, sed diam nonummy nibh euismod tincidunt ut laoreet dolore magna aliquam erat volutpat.</p>
<p class="abs card-copy" style="left:381px;top:724px">Lorem ipsum dolor sit amet, consectetuer adipiscing elit, sed diam nonummy nibh euismod tincidunt ut laoreet dolore magna aliquam erat volutpat.</p>
<p class="abs card-copy" style="left:570px;top:724px">Lorem ipsum dolor sit amet, consectetuer adipiscing elit, sed diam nonummy nibh euismod tincidunt ut laoreet dolore magna aliquam erat volutpat.</p>
<p class="abs card-copy" style="left:763px;top:724px">Lorem ipsum dolor sit amet, consectetuer adipiscing elit, sed diam nonummy nibh euismod tincidunt ut laoreet dolore magna aliquam erat volutpat.</p>

<div class="abs read-more" style="left:192px;top:779px;width:96px">READ MORE</div>
<div class="abs read-more" style="left:381px;top:779px;width:96px">READ MORE</div>
<div class="abs read-more" style="left:572px;top:779px;width:96px">READ MORE</div>
<div class="abs read-more" style="left:762px;top:779px;width:96px">READ MORE</div>

<footer>
  <div class="abs footer-zone"></div>
  <div class="abs help"></div>
  <div class="abs help-h">How can<br><span>I help you</span><em>?</em></div>
  <div class="abs help-line"></div>
  <div class="abs help-sub">We are here to help you</div>
  <div class="abs help-hours">Monday - Friday: 10:00am - 6pm<br>Saturday: 10:00am - Noon<br><br>Lorem ipsum dolor sit amet.</div>
  <div class="abs chat">Chat with us</div>
  <div class="abs address">Kenda.4417 Ridgeline Road,<br>Lorem Ipsum<br><span>Telephone:</span> +1 555 014 2286<br><span>FAX:</span> +1 555 014 2287</div>
  <div class="abs foot-social" style="left:191px"></div>
  <div class="abs foot-social" style="left:216px"></div>

  <div class="abs clients"></div>
  <div class="abs sec-h" style="left:396px;top:854px">OUR <span>CLIENTS</span></div>
  <div class="abs" style="left:395px;top:879px;font-size:11px;color:#ccc">Donec ac condimentum erat. Donec malesuada sagittis.</div>
  <div class="abs dots" style="left:396px;top:905px"></div>
  <div class="abs client-name" style="left:397px">HARBORLY</div>
  <div class="abs client-name" style="left:526px">VELDTRON</div>
  <div class="abs client-name" style="left:666px">Orin Pell</div>
  <div class="abs client-name" style="left:794px">Kestrova</div>
  <div class="abs dots" style="left:396px;top:961px"></div>
  <div class="abs sec-h" style="left:396px;top:978px">OUR <span>REVIRWS</span></div>
  <p class="abs review">‘Duis autem vel eum iriure dolor in hendrerit in vulputate velit esse molestie consequat, vel illum<br>dolore eu feugiat nulla facilisis at vero eros et accumsan et iusto.’<span class="review-dots">........................................................</span></p>
  <div class="abs reviewer">Mr. D. Okafor Lind<br><span>Lorem Ipsum</span></div>
  <div class="abs find-more">FIND MORE</div>

  <div class="abs foot-nav"><span>Who we are</span><span>Services</span><span>Careers</span><span>Owners</span><span>Our Updates</span><span>Contact Us</span></div>
  <div class="abs copyright">HaulvergeKenda © 2012 Privacy Policy</div>
</footer>
</body>
</html>
```